Label design for an exciting new Vodka brand

We need a label design for a dynamic new Vodka brand called 'Tall amber fern Vodka'. It is a crisp and versatile liquid with a clean and smooth finish. It should appeal to 21-39 year olds, with a slight female skew. Colours, fonts and styles should be modern and relatively neutral - take inspiration from the brand pictures attached.

Target Market(s)

21-39 year olds, both male and female, but with a slight female skew

```html
<!DOCTYPE html>
<html lang="en">
<head>
<meta charset="utf-8">
<title>Tall amber fern Vodka – Label</title>
<link href="https://fonts.googleapis.com/css2?family=Oswald:wght@500;700&display=swap" rel="stylesheet">
<style>
  :root {
    --stage: #f5f5f5;
    --label-bg: #f9e8e3;
    --coral: #ee9276;
    --coral-light: #f2a68e;
    --gold-light: #f7e7a6;
    --gold-mid: #e0bd55;
    --gold-deep: #b98a22;
    --ink: #1d1d1d;
  }
  * { margin: 0; padding: 0; box-sizing: border-box; }
  html, body {
    width: 1200px;
    height: 675px;
    overflow: hidden;
    background: var(--stage);
  }
  .stage {
    width: 1200px;
    height: 675px;
    display: flex;
    align-items: center;
    justify-content: center;
  }
  .label {
    position: relative;
    width: 460px;
    height: 560px;
    background: var(--label-bg);
    font-family: "Oswald", sans-serif;
    box-shadow: 0 2px 14px rgba(0,0,0,0.06);
  }
  .seal {
    position: absolute;
    top: 24px;
    right: 28px;
    width: 96px;
    height: 96px;
  }
  .brand-name {
    position: absolute;
    top: 170px;
    left: 0;
    width: 100%;
    text-align: center;
    font-weight: 700;
    font-size: 64px;
    line-height: 1.05;
    letter-spacing: 0.5px;
    color: var(--coral);
    text-transform: uppercase;
  }
  .brand-name span { display: block; }
  .foil {
    background: linear-gradient(160deg, var(--gold-light) 0%, var(--gold-mid) 45%, var(--gold-deep) 100%);
    -webkit-background-clip: text;
    background-clip: text;
    color: transparent;
  }
  .tagline {
    position: absolute;
    top: 456px;
    left: 0;
    width: 100%;
    text-align: center;
    font-weight: 500;
    font-size: 19px;
    line-height: 1.05;
    letter-spacing: -0.2px;
    color: var(--coral-light);
    text-transform: uppercase;
  }
  .volume {
    position: absolute;
    top: 522px;
    left: 0;
    width: 100%;
    text-align: center;
    font-weight: 700;
    font-size: 12px;
    color: var(--ink);
  }
</style>
</head>
<body>
  <main class="stage">
    <section class="label">
      <svg class="seal" viewBox="0 0 120 120" aria-hidden="true">
        <defs>
          <radialGradient id="seal-gold" cx="35%" cy="30%" r="75%">
            <stop offset="0%" stop-color="#fbf1c8"/>
            <stop offset="45%" stop-color="#e2c05c"/>
            <stop offset="100%" stop-color="#a97b1c"/>
          </radialGradient>
        </defs>
        <circle cx="60" cy="60" r="58" fill="url(#seal-gold)"/>
      </svg>

      <h1 class="brand-name">
        <span>Tall amber</span>
        <span>fern vodka</span>
      </h1>

      <p class="tagline">Crisp and versatile with a<br>clean and <span class="foil">smoooth</span> finish</p>
      <p class="volume">700ML</p>
    </section>
  </main>
</body>
</html>
```